Foldable creative restaurant menu

We require foldable restaurant menu to be placed on the each table, want it to look creative and modern with pages representing pictures of the dish not all dishes but few to represent what we do.Please get creative make sure its different, the colour should represent classy restaurant, not cheap and fast. The shape of the menu can be difference creative words must be easy to read and the logo must be in the menu here and there briefly.

Target Market(s)

Restaurant customers

Industry/Entity Type

Health And Wellness

Colors

Designer to choose colors to be used in the design.

Requirements
Must have
• foldable, must have good dish presentation pictures and must look modern and classy
Nice to have
• funky design and creative can be not just square foldable but can be interesting shape of menu.
Should not have
• boring plain spaces
• small writing
• dark pictures

```html
<!DOCTYPE html>
<html lang="en">
<head>
<meta charset="utf-8">
<title>Verdelle Restaurant – Bistro Menu</title>
<link rel="stylesheet" href="https://fonts.googleapis.com/css2?family=Josefin+Sans:wght@200;300;400;600&display=swap">
<style>
  :root {
    --backdrop: #dcdcdc;
    --leaf: #2f8a35;
    --leaf-deep: #257a2c;
    --leaf-light: #5cbf62;
    --paper: #ffffff;
    --ink: #1f1f1f;
    --ink-soft: #555555;
    --line-on-green: rgba(255,255,255,0.75);
    --line-on-paper: rgba(0,0,0,0.12);
  }
  * { box-sizing: border-box; margin: 0; padding: 0; }
  html, body { width: 681px; height: 1200px; overflow: hidden; }
  body {
    background: var(--backdrop);
    font-family: "Josefin Sans", "Century Gothic", sans-serif;
    color: var(--ink);
    position: relative;
  }
  .spread {
    position: absolute;
    left: 12px;
    width: 657px;
    height: 565px;
    display: flex;
    gap: 6px;
  }
  .spread--outside { top: 18px; }
  .spread--inside { top: 612px; }

  .menu-panel {
    position: relative;
    width: 215px;
    height: 100%;
    border-radius: 108px 108px 0 0;
    overflow: hidden;
    padding: 40px 16px 12px;
  }
  .panel--paper { background: var(--paper); }
  .panel--green { background: linear-gradient(160deg, var(--leaf) 0%, var(--leaf-deep) 100%); color: #fff; }
  .panel--breakfast { background: linear-gradient(180deg, var(--leaf-deep) 0%, var(--leaf-light) 100%); color: #fff; }

  .ornament { position: absolute; inset: 0; width: 100%; height: 100%; pointer-events: none; }
  .content { position: relative; }

  .section-title {
    font-weight: 300;
    font-size: 21px;
    letter-spacing: 1px;
    text-align: center;
    color: var(--leaf);
    margin: 4px 0 8px;
  }
  .panel--green .section-title, .panel--breakfast .section-title { color: #fff; }

  .dish { margin-bottom: 7px; }
  .dish-name {
    font-weight: 600;
    font-size: 7.4px;
    text-transform: uppercase;
    letter-spacing: 0.2px;
  }
  .price { margin-left: 6px; font-weight: 400; }
  .dish-desc { font-size: 6.4px; line-height: 1.3; color: var(--ink-soft); font-weight: 300; }
  .panel--green .dish-desc, .panel--breakfast .dish-desc { color: rgba(255,255,255,0.9); }
  .dish-options { font-size: 6.2px; line-height: 1.35; font-weight: 300; padding-left: 8px; }

  .photo { border-radius: 4px; }
  .photo--salad {
    position: absolute; left: 0; right: 0; bottom: 0; height: 190px;
    background: radial-gradient(ellipse at 55% 45%, #6e9f3c 0%, #3d6b27 55%, #c85a3a 80%, #f2f2f2 100%);
    border-radius: 0;
  }
  .photo--sandwich {
    height: 112px; margin: 0 6px 4px;
    background: radial-gradient(ellipse at 40% 50%, #c99a55 0%, #a97b3d 45%, #f0eee8 70%);
    border: 4px solid #fff;
  }
  .photo--parmigiana {
    position: absolute; left: 14px; right: 14px; bottom: 14px; height: 150px;
    background: radial-gradient(ellipse at 40% 45%, #f4e2a8 0%, #d6a45a 40%, #5f8e3a 75%, #f3f3f3 100%);
    border: 3px solid #fff; box-shadow: 0 1px 4px rgba(0,0,0,0.2);
  }

  .cover { text-align: center; padding-top: 28px; }
  .brand-name { font-weight: 200; font-size: 30px; letter-spacing: 3px; }
  .brand-tag { font-weight: 300; font-size: 11px; letter-spacing: 4px; margin-top: 8px; }
  .cover-title { font-weight: 200; font-size: 29px; line-height: 1.15; margin-top: 92px; letter-spacing: 1px; }

  .bev-title { font-size: 18px; }
  .bev .dish-name { font-size: 6.8px; }
  .bev .dish-desc { font-size: 5.8px; }

  .sides-list .dish-name, .kids-list .dish-name { margin-bottom: 7px; }
</style>
</head>
<body>

<section class="spread spread--outside">
  <article class="menu-panel panel--paper">
    <svg class="ornament" viewBox="0 0 215 565"><circle cx="170" cy="330" r="120" fill="none" stroke="var(--line-on-paper)" stroke-width="0.8"/><circle cx="22" cy="270" r="6" fill="none" stroke="var(--line-on-paper)" stroke-width="0.8"/></svg>
    <div class="content">
      <h2 class="section-title">SALAD</h2>
      <div class="dish"><p class="dish-name">Asian Chicken Fusion Salad<span class="price">15</span></p><p class="dish-desc">Grilled chicken served with a medley of fresh salad greens, sesame nut crumb and a light sweet chilli, sesame and soy dressing</p></div>
      <div class="dish"><p class="dish-name">Caesar Salad<span class="price">15</span></p><p class="dish-desc">Baby cos lettuce, crispy bacon, garlic croutons, flaked parmesan cheese, boiled egg in Caesar dressing<br>ADD CHICKEN 4 – SMOKED SALMON 5</p></div>
      <div class="dish"><p class="dish-name">House Salad<span class="price">10</span></p><p class="dish-desc">Crispy lettuce mix, tomato, cucumber, spinach, red onion, Kalamata olives and feta cheese drizzled with house dressing<br>ADD CHICKEN 4 – SMOKED SALMON 5</p></div>
      <h2 class="section-title">PASTA</h2>
      <div class="dish"><p class="dish-name">Fettuccine Carbonara<span class="price">15</span></p><p class="dish-desc">Fettuccine served with pan seared sliced ham, bacon, shallots and onion in a creamy garlic sauce</p></div>
      <div class="dish"><p class="dish-name">Fettuccine Matriciana – V<span class="price">15</span></p><p class="dish-desc">Fettuccine served with sun dried tomatoes, capsicum, zucchini, mushroom, onion, shallot and garlic in a Napoli sauce</p></div>
      <div class="dish"><p class="dish-name">Spaghetti Bolognese<span class="price">15</span></p><p class="dish-desc">Spaghetti cooked al dente and pan tossed with a traditional Italian style meat sauce</p></div>
    </div>
    <div class="photo photo--salad" role="img" aria-label="Photo of a fresh green leaf salad with carrot and crispy noodles in a white bowl"></div>
  </article>

  <article class="menu-panel panel--green bev">
    <svg class="ornament" viewBox="0 0 215 565"><circle cx="200" cy="520" r="80" fill="none" stroke="var(--line-on-green)" stroke-width="0.8"/><circle cx="70" cy="480" r="5" fill="none" stroke="var(--line-on-green)" stroke-width="0.8"/></svg>
    <div class="content">
      <h2 class="section-title bev-title">BEVERAGES</h2>
      <div class="dish"><p class="dish-name">Soft Drinks 500ml<span class="price">4</span> &nbsp;Jug<span class="price">8</span></p><p class="dish-desc">Cola, lemonade, orange, ginger beer, raspberry lemonade, lemon lime &amp; bitters, soda lime &amp; bitters</p></div>
      <div class="dish"><p class="dish-name">Mineral Water</p><p class="dish-desc">Still spring water 600ml 4<br>Sparkling lemon or lime 3<br>Coconut water 330ml 4</p></div>
      <div class="dish"><p class="dish-name">Fresh Squeezed Juices</p><p class="dish-desc">Orange juice 250ml 4 &nbsp; 500ml 8</p></div>
      <div class="dish"><p class="dish-name">Smoothies</p><p class="dish-desc">Acai 9 — choice of:<br>(1) Berry boost – acai, banana and almond milk or apple juice<br>(2) Tropical – coconut, mango, banana, frozen mixed berries and coconut water</p></div>
      <div class="dish"><p class="dish-name">Lean &amp; Green</p><p class="dish-desc">Kale, spinach, cucumber, celery &amp; banana 9<br>Mango – mango, yoghurt, milk &amp; honey 8<br>Banana – banana, yoghurt, milk, honey &amp; cinnamon 8<br>Mixed berry – berries, yoghurt, milk &amp; honey 8</p></div>
      <div class="dish"><p class="dish-name">Milkshakes<span class="price">8</span></p><p class="dish-desc">Chocolate, strawberry, caramel</p></div>
      <div class="dish"><p class="dish-name">Thickshakes<span class="price">10</span></p></div>
    </div>
  </article>

  <article class="menu-panel panel--green">
    <svg class="ornament" viewBox="0 0 215 565"><circle cx="170" cy="130" r="95" fill="none" stroke="var(--line-on-green)" stroke-width="0.8"/><circle cx="100" cy="290" r="85" fill="none" stroke="var(--line-on-green)" stroke-width="0.8"/><circle cx="200" cy="505" r="6" fill="none" stroke="var(--line-on-green)" stroke-width="0.8"/></svg>
    <div class="content cover">
      <h1 class="brand-name">Verdelle</h1>
      <p class="brand-tag">RESTAURANT</p>
      <p class="cover-title">BISTRO<br>MENU</p>
    </div>
  </article>
</section>

<section class="spread spread--inside">
  <article class="menu-panel panel--breakfast">
    <svg class="ornament" viewBox="0 0 215 565"><circle cx="200" cy="95" r="5" fill="none" stroke="var(--line-on-green)" stroke-width="0.8"/></svg>
    <div class="content">
      <div class="photo photo--sandwich" role="img" aria-label="Photo of a toasted seeded sandwich with egg on a white plate"></div>
      <h2 class="section-title">BREAKFAST</h2>
      <div class="dish"><p class="dish-name">Big Verdelle Breakfast<span class="price">19</span></p><p class="dish-desc">Choose from sourdough or Turkish served with eggs, bacon, chipolata, hash brown, spinach, tomato &amp; mushroom</p></div>
      <div class="dish"><p class="dish-name">Acai Bowl<span class="price">13</span></p><p class="dish-options">(1) Zesty Detox – acai, raspberries, banana, apple juice<br>(2) Antioxidant – acai, berries, avocado, coconut water<br>(3) Tropical Fest – acai, mango, coconut water<br>(4) Cocolicious – coconut, banana, coconut water</p></div>
      <div class="dish"><p class="dish-name">Avocado Smash – V GF<span class="price">13</span></p><p class="dish-desc">Feta, spinach &amp; avocado served on sourdough</p></div>
      <div class="dish"><p class="dish-name">Eggs Benedict<span class="price">10</span></p><p class="dish-desc">Poached eggs, English muffin, sautéed baby spinach served with hollandaise</p></div>
      <div class="dish"><p class="dish-name">Egg &amp; Bacon Roll<span class="price">10</span></p></div>
      <div class="dish"><p class="dish-name">Add On's</p><p class="dish-desc">Spinach 2, Mushroom 2, Egg 2, Cheese 2, Avocado 3, Bacon 3, Ham 3, Chipolata 3, Smoked salmon 5</p></div>
      <div class="dish"><p class="dish-name">Bruschetta<span class="price">12</span></p><p class="dish-desc">Toast served with tangy tomatoes, basil, red onion and garlic with feta and balsamic dressing</p></div>
      <div class="dish"><p class="dish-name">7-Seed Breakfast<span class="price">10</span></p><p class="dish-desc">Low gluten seeded bread with scrambled egg, four leaf salad and cherry tomatoes with feta</p></div>
    </div>
  </article>

  <article class="menu-panel panel--paper">
    <svg class="ornament" viewBox="0 0 215 565"><circle cx="40" cy="220" r="150" fill="none" stroke="var(--line-on-paper)" stroke-width="0.8"/><circle cx="108" cy="138" r="5" fill="none" stroke="var(--line-on-paper)" stroke-width="0.8"/></svg>
    <div class="content">
      <h2 class="section-title">MAINS</h2>
      <div class="dish"><p class="dish-name">Salmon Skin On<span class="price">25</span></p><p class="dish-desc">Salmon fillet served the way you like it, with two choices of chips, salad or steamed vegetables<br>ADD Sauce – hollandaise, lemon butter</p></div>
      <div class="dish"><p class="dish-name">Steak of the Day<span class="price">25</span></p><p class="dish-desc">Steak cooked rare, medium or well done with two choices of chips, salad or vegetables<br>ADD Sauce – pepper, mushroom or garlic</p></div>
      <div class="dish"><p class="dish-name">Barramundi Fillet<span class="price">23</span></p><p class="dish-desc">Barramundi fillet on a bed of rice with creamy white wine sauce<br>ADD Sauce – lemon butter</p></div>
      <div class="dish"><p class="dish-name">Italian Style Breastfillet with pesto sauce<span class="price">23</span></p><p class="dish-desc">Grilled chicken breast with steamed vegetables and pesto cream</p></div>
      <div class="dish"><p class="dish-name">Chicken Parmigiana<span class="price">17</span></p><p class="dish-desc">Crumbed chicken breast topped with Napoli sauce, ham and cheese, with chips and salad</p></div>
      <div class="dish"><p class="dish-name">Chicken Carbonara Parmigiana<span class="price">17</span></p><p class="dish-desc">Crumbed chicken breast topped with bacon, garlic cream sauce and cheese, with chips and salad</p></div>
      <div class="dish"><p class="dish-name">Classic Beef Burger<span class="price">15</span></p><p class="dish-desc">Beef patty with cheese, bacon, lettuce and tomato with chips<br>Choice of sauce – tomato, BBQ or relish</p></div>
      <div class="dish"><p class="dish-name">Soup of the Day<span class="price">8</span></p></div>
    </div>
    <div class="photo photo--parmigiana" role="img" aria-label="Photo of chicken parmigiana with melted cheese, chips and garden salad on a white plate"></div>
  </article>

  <article class="menu-panel panel--paper">
    <svg class="ornament" viewBox="0 0 215 565"><circle cx="200" cy="200" r="90" fill="none" stroke="var(--line-on-paper)" stroke-width="0.8"/><circle cx="185" cy="420" r="80" fill="none" stroke="var(--line-on-paper)" stroke-width="0.8"/><circle cx="190" cy="378" r="6" fill="none" stroke="var(--line-on-paper)" stroke-width="0.8"/></svg>
    <div class="content" style="padding-top:8px">
      <div class="dish"><p class="dish-name">Club Sandwich<span class="price">20</span></p><p class="dish-desc">Big 3 layers sandwich with chicken, bacon, eggs, tomato and lettuce, served with chips</p></div>
      <div class="dish"><p class="dish-name">Lamb Shank<span class="price">25</span></p><p class="dish-desc">Slow cooked lamb shank served with mashed potato &amp; vegetables in tomato red wine herb sauce</p></div>
      <div class="dish"><p class="dish-name">Roast of the Day (beef or pork)<span class="price">25</span></p><p class="dish-desc">Roasted pork or beef with mashed potato and vegetables with gravy sauce</p></div>
      <div class="dish"><p class="dish-name">Mushroom Risotto<span class="price">20</span></p><p class="dish-desc">Vegetarian mushroom risotto with Arborio rice</p></div>
      <div class="dish"><p class="dish-name">Pork Scallopini<span class="price">23</span></p><p class="dish-desc">Medallions of pork fried in a mushroom white wine sauce with steamed vegetables and mashed potato</p></div>
      <div class="dish"><p class="dish-name">Nachos<span class="price">16</span></p><p class="dish-desc">Corn chips, beef, salsa, tasty cheese, grilled to perfection</p></div>
      <div class="dish"><p class="dish-name">Salt and Pepper Squid<span class="price">15</span></p><p class="dish-desc">Squid, wedges with light sour cream and sweet chilli sauce</p></div>
      <div class="dish"><p class="dish-name">Fish and Chips<span class="price">12</span></p><p class="dish-desc">Fish, chips, salad and tartar sauce</p></div>
      <h2 class="section-title">SIDES</h2>
      <div class="sides-list">
        <p class="dish-name">Chips<span class="price">4</span></p>
        <p class="dish-name">Garden Salad<span class="price">6</span></p>
        <p class="dish-name">Rice<span class="price">3</span></p>
      </div>
      <h2 class="section-title">KID'S MEALS</h2>
      <div class="kids-list">
        <div class="dish"><p class="dish-name">Cardinale Pizza &amp; Chips<span class="price">10</span></p><p class="dish-desc">Mozzarella cheese and ham served with chips</p></div>
        <p class="dish-name">Spaghetti Bolognese<span class="price">7</span></p>
        <p class="dish-name">Spaghetti with Meatballs<span class="price">7</span></p>
        <p class="dish-name">Cheeseburger and Chips<span class="price">7</span></p>
        <p class="dish-name">Fish and Chips<span class="price">7</span></p>
        <p class="dish-name">Chips and Nuggets<span class="price">7</span></p>
      </div>
    </div>
  </article>
</section>

</body>
</html>
```